RM Cargoline businesscard project

RM Cargoline Ltd is a freshly founded small (3 employees), young (average age is 30 years) company, living from the road transportation market without own tools.
We would like to have an impressive, new-line, cool busines card for a freshly founded forwarding company on an overcrowded market which raises attention and makes the potential partners eager to work with us.

Target Market(s)

The main profile of the company is logistic/forwarding on road.

Industry/Entity Type

Freight Forwarding

Contact Information for Business Card

Name: Berki Zsófia
Title: general manager
mobile nr: +36-70/482-5193
fax nr: +36-1/534-9061
e-mail: zsofia.berki@rmcargoline.example
info@rmcargoline.example
website address: http://www.rmcargoline.example
and if possible maybe some funny or helpful info on the back

Requirements
Must have
• contact details above
Nice to have
• some really nice and catching back-side (info, graphics, useful tool info... anything)
Should not have
• trucks, road, ship, airplane on it...

```html
<!DOCTYPE html>
<html lang="hu">
<head>
<meta charset="utf-8">
<title>RM Cargoline – Business Card</title>
<link rel="stylesheet" href="https://fonts.googleapis.com/css2?family=Fjalla+One&family=Lato:wght@400;700&display=swap">
<style>
  :root {
    --navy: #0e1460;
    --navy-deep: #0b1050;
    --white: #ffffff;
    --paper: #f4f4f2;
    --backdrop: #e9e6e1;
    --rule: rgba(255,255,255,0.75);
    --muted: #d7d9ec;
  }
  * { margin: 0; padding: 0; box-sizing: border-box; }
  html, body {
    width: 1200px; height: 900px; overflow: hidden;
    background: var(--backdrop);
  }
  .canvas { position: relative; width: 1200px; height: 900px; }

  .card {
    position: absolute;
    width: 560px; height: 320px;
    overflow: hidden;
    box-shadow: 0 10px 28px rgba(0,0,0,0.22);
    font-family: "Lato", Arial, sans-serif;
  }

  /* Front */
  .card-front { left: 60px; top: 80px; background: var(--navy); }
  .front-band {
    position: absolute; left: 0; top: 0; width: 100%; height: 112px;
    background: var(--paper);
  }
  .front-wordmark {
    position: absolute; right: 40px; top: 22px;
    font-family: "Fjalla One", "Arial Narrow", sans-serif;
    font-size: 50px; line-height: 1; color: var(--navy);
  }
  .front-brand {
    position: absolute; left: 34px; top: 176px;
    font-family: "Fjalla One", "Arial Narrow", sans-serif;
    font-size: 38px; line-height: 1; color: var(--white);
  }
  .front-rule {
    position: absolute; left: 290px; right: 30px; top: 126px;
    height: 1px; background: var(--rule);
  }
  .person { position: absolute; left: 290px; top: 136px; color: var(--white); }
  .person-name { font-size: 21px; font-weight: 400; letter-spacing: 0.2px; }
  .person-name b { font-weight: 700; }
  .person-title { font-size: 11px; color: var(--muted); margin-top: 1px; }

  .contact-list {
    position: absolute; left: 290px; top: 196px;
    list-style: none; color: var(--white); font-size: 14.5px; line-height: 18px;
  }
  .contact-item { display: flex; align-items: flex-start; gap: 8px; margin-bottom: 2px; }
  .contact-icon { width: 12px; height: 12px; margin-top: 3px; flex: none; fill: var(--white); }
  .contact-lines { display: flex; flex-direction: column; }

  /* Back */
  .card-back {
    left: 580px; top: 500px;
    background: radial-gradient(ellipse at 55% 35%, #16207a 0%, var(--navy) 55%, var(--navy-deep) 100%);
  }
  .back-brand {
    position: absolute; left: 40px; bottom: 40px;
    display: flex; align-items: center; gap: 12px;
  }
  .back-brand-square { width: 26px; height: 26px; background: var(--white); }
  .back-brand-name {
    font-family: "Fjalla One", "Arial Narrow", sans-serif;
    font-size: 30px; line-height: 1; color: var(--white);
  }
  .back-web {
    position: absolute; right: 40px; bottom: 110px;
    display: flex; align-items: center; gap: 8px;
    color: var(--white); font-size: 14.5px;
  }
</style>
</head>
<body>
<main class="canvas">

  <section class="card card-front" aria-label="Business card front">
    <div class="front-band"></div>
    <div class="front-wordmark">RM Cargoline</div>
    <div class="front-brand">RM Cargoline</div>
    <div class="front-rule"></div>

    <div class="person">
      <div class="person-name"><b>BERKI</b> ZSÓFIA</div>
      <div class="person-title">General Manager</div>
    </div>

    <ul class="contact-list">
      <li class="contact-item">
        <svg class="contact-icon" viewBox="0 0 12 12" aria-hidden="true"><path d="M1 4.5C1 2.5 3 1.5 6 1.5s5 1 5 3v1H8.5V4.2c-.8-.3-1.6-.4-2.5-.4s-1.7.1-2.5.4v1.3H1z M3 6.5h6l1 4H2z"/></svg>
        <span>+36-70/482-5193</span>
      </li>
      <li class="contact-item">
        <svg class="contact-icon" viewBox="0 0 12 12" aria-hidden="true"><path d="M3 1h6v3H3z M1 5h10v5H9V8H3v2H1z M3.5 8.8h5V11h-5z"/></svg>
        <span>+36-1/534-9061</span>
      </li>
      <li class="contact-item">
        <svg class="contact-icon" viewBox="0 0 12 12" aria-hidden="true"><path d="M1 2.5h10v7H1z" fill="none" stroke="#fff" stroke-width="1.2"/><path d="M1 2.5l5 4 5-4" fill="none" stroke="#fff" stroke-width="1.2"/></svg>
        <span class="contact-lines"><span>zsofia.berki@rmcargoline.example</span><span>info@rmcargoline.example</span></span>
      </li>
      <li class="contact-item">
        <svg class="contact-icon" viewBox="0 0 12 12" aria-hidden="true"><g fill="none" stroke="#fff" stroke-width="1"><circle cx="6" cy="6" r="5"/><ellipse cx="6" cy="6" rx="2.2" ry="5"/><path d="M1 6h10M2 3.5h8M2 8.5h8"/></g></svg>
        <span>www.rmcargoline.example</span>
      </li>
    </ul>
  </section>

  <section class="card card-back" aria-label="Business card back">
    <div class="back-web">
      <svg class="contact-icon" viewBox="0 0 12 12" aria-hidden="true" style="margin-top:0"><g fill="none" stroke="#fff" stroke-width="1"><circle cx="6" cy="6" r="5"/><ellipse cx="6" cy="6" rx="2.2" ry="5"/><path d="M1 6h10M2 3.5h8M2 8.5h8"/></g></svg>
      <span>www.rmcargoline.example</span>
    </div>
    <div class="back-brand">
      <div class="back-brand-square"></div>
      <div class="back-brand-name">RM Cargoline</div>
    </div>
  </section>

</main>
</body>
</html>
```